Jewelry Shop Needs a Business Card Design

***We want a very sharp and unforgettable pantone for the Business Card. ***
***We do not want the business card or logo only in black, white and grey color!!!Please provide us a main color as our brand topic! Thanks!! ***

Mabel’s Nook is a Hong Kong based fine jewelry brand.

We want a very nice, simple and elegant business card design for Mabel's Nook Brand. The company's logo has been uploaded already.

You can design with below info:

Dorian Fung
Director
M: +852 94273658
T: +852 35820417
F: +852 35820419
E: dorian.fung@mabelsnook.example
5/F , Harbourlight Tower, 12-18 Orchid Lane, Wan Tung Kok, Kowloon, Hong Kong

Target Market(s)

Mabel’s Nook philosophy is a jewelry icon of young, creative, trendy, fashionable, stylish, energetic, and elegant. For Mabel’s Nook, jewelry is one collection of artworks, the most important items in personal life.

Industry/Entity Type

Jewelry

Requirements
Must have
• We want a very sharp and unforgettable pantone for the Business Card.

```html
<!DOCTYPE html>
<html lang="en">
<head>
<meta charset="UTF-8">
<title>Mabel's Nook — Business Card</title>
<link rel="stylesheet" href="https://fonts.googleapis.com/css2?family=Open+Sans:wght@400;600&display=swap">
<style>
  :root {
    --page-bg: #e9e9e9;
    --teal-top: #1cc2c0;
    --green-mid: #1aa64a;
    --blue-bottom: #1e8fe0;
    --gold-line: #b7a94a;
    --navy-disc: #1b2440;
    --back-green: #17925f;
    --accent-teal: #1fb3a4;
    --text-light: #e8f5ee;
    --text-soft: #b9e3cc;
    --white: #ffffff;
  }
  * { box-sizing: border-box; margin: 0; padding: 0; }
  html, body {
    width: 1200px; height: 1200px; overflow: hidden;
    background: radial-gradient(circle at 40% 30%, #f7f7f7 0%, var(--page-bg) 70%, #d6d6d6 100%);
  }
  .canvas {
    width: 1200px; height: 1200px;
    display: flex; flex-direction: column; align-items: center; justify-content: center;
    gap: 70px;
  }
  .card {
    position: relative;
    width: 700px; height: 400px;
    border-radius: 4px;
    overflow: hidden;
    box-shadow: 0 18px 40px rgba(0,0,0,0.18);
  }

  /* Front */
  .card-front {
    background: linear-gradient(170deg, var(--teal-top) 0%, #1bb38a 28%, var(--green-mid) 55%, #1c9bb0 78%, var(--blue-bottom) 100%);
  }
  .front-rule {
    position: absolute; left: 0; right: 0; top: 239px;
    height: 2px; background: var(--gold-line); opacity: 0.85;
  }
  .front-disc {
    position: absolute; left: 308px; top: 148px;
    width: 84px; height: 84px; border-radius: 50%;
    background: var(--navy-disc);
  }
  .front-name {
    position: absolute; left: 0; right: 0; top: 250px;
    text-align: center;
    font-family: "Open Sans", sans-serif; font-weight: 600;
    font-size: 22px; letter-spacing: 0.5px;
    color: var(--navy-disc);
  }

  /* Back */
  .card-back { background: var(--back-green); }
  .back-accent-top {
    position: absolute; left: 80px; top: 0; width: 14px; height: 40px;
    background: var(--accent-teal);
  }
  .back-accent-bottom {
    position: absolute; left: 80px; bottom: 0; width: 14px; height: 30px;
    background: var(--accent-teal);
  }
  .contact {
    position: absolute; left: 80px; top: 60px;
    font-family: "Open Sans", sans-serif; color: var(--text-light);
  }
  .person-name { font-weight: 600; font-size: 22px; line-height: 1.2; }
  .person-title { font-size: 13px; color: var(--text-soft); margin-bottom: 22px; }
  .address { font-size: 15px; line-height: 1.35; margin-bottom: 20px; }
  .lines { list-style: none; font-size: 15px; line-height: 1.5; }
  .lines li { display: flex; align-items: center; gap: 10px; }
  .icon { width: 16px; height: 16px; flex: none; }
  .back-brand {
    position: absolute; right: 48px; bottom: 40px;
    display: flex; flex-direction: column; align-items: center; gap: 10px;
  }
  .back-disc {
    width: 62px; height: 62px; border-radius: 50%; background: var(--white);
  }
  .back-name {
    font-family: "Open Sans", sans-serif; font-weight: 600;
    font-size: 14px; letter-spacing: 0.5px; color: var(--white);
  }
</style>
</head>
<body>
<main class="canvas">

  <section class="card card-front" aria-label="Card front">
    <div class="front-rule"></div>
    <div class="front-disc"></div>
    <div class="front-name">Mabel’s Nook</div>
  </section>

  <section class="card card-back" aria-label="Card back">
    <div class="back-accent-top"></div>
    <div class="back-accent-bottom"></div>
    <div class="contact">
      <div class="person-name">Dorian Fung</div>
      <div class="person-title">Director</div>
      <p class="address">5/F , Harbourlight Tower,<br>12-18 Orchid Lane, Wan Tung Kok,<br>Kowloon, Hong Kong</p>
      <ul class="lines">
        <li>
          <svg class="icon" viewBox="0 0 16 16" aria-hidden="true"><rect x="0.5" y="0.5" width="15" height="15" rx="3" fill="none" stroke="currentColor" opacity="0.7"/><rect x="5" y="3" width="6" height="10" rx="1" fill="currentColor"/></svg>
          +852 94273658
        </li>
        <li>
          <svg class="icon" viewBox="0 0 16 16" aria-hidden="true"><rect x="0.5" y="0.5" width="15" height="15" rx="3" fill="none" stroke="currentColor" opacity="0.7"/><path d="M4 5c0-1 1-2 2-1l1 2-1 1c.6 1.3 1.7 2.4 3 3l1-1 2 1c1 1 0 2-1 2-4 0-7-3-7-7z" fill="currentColor"/></svg>
          +852 35820417
        </li>
        <li>
          <svg class="icon" viewBox="0 0 16 16" aria-hidden="true"><rect x="0.5" y="0.5" width="15" height="15" rx="3" fill="none" stroke="currentColor" opacity="0.7"/><rect x="5" y="3" width="6" height="3" fill="currentColor"/><rect x="3" y="7" width="10" height="5" rx="1" fill="currentColor"/></svg>
          +852 35820419
        </li>
        <li>
          <svg class="icon" viewBox="0 0 16 16" aria-hidden="true"><rect x="0.5" y="0.5" width="15" height="15" rx="3" fill="none" stroke="currentColor" opacity="0.7"/><rect x="3" y="4.5" width="10" height="7" rx="1" fill="none" stroke="currentColor"/><path d="M3 5l5 4 5-4" fill="none" stroke="currentColor"/></svg>
          dorian.fung@mabelsnook.example
        </li>
      </ul>
    </div>
    <div class="back-brand">
      <div class="back-disc"></div>
      <div class="back-name">Mabel’s Nook</div>
    </div>
  </section>

</main>
</body>
</html>
```